In Home Senior Care Agency Business Card Design Needed

At Silver Birch Helpers, we don't just work in the care-giving industry. We truly care.

We are dedicated to providing personable, hands-on and integrated caring services that aim to help people maintain safe and comfortable life standards within the familiar settings of their own homes.

We would like to see designs that use my logo colors obviously. The final design will be modern, yet professional and semi-minimalistic. It should communicate an well-established company that is innovative. We would also like the design to have that 'flat' design look. Ideally having the design roll over to the backend of the card. Most likely it will be printed on a Matte paper with a die cut (either 2 rounded corners -leaf cut) or all rounded.

Target Market(s)

Baby boomer generation. 45 years and older.

Industry/Entity Type

Business

Contact Information for Business Card

Text for Front:
Slogan somewhere "Our Family. Caring For Yours.”

Darren Whitlow
President

Cell: 917.284.6051
Phone: 917.512.7368
E: Darren@silverbirchhelpers.com
W: www.SilverBirchHelpers.com

Back:
-Meal Preparation
-Transportation
-Light Housekeeping
-Bathing Assistance
-Companionship

Font styles to use
Serif
Sans Serif

Requirements
Must have
• Flat, modern, professional design. Not too many colors. Match my colors in logo. Design of card must reflect from the front onto the back. Evenly spaced font.
Nice to have
• Try to work off current logo scheme, but logo may need to be redesigned.
Should not have
• Not too many colors.

```html
<!DOCTYPE html>
<html lang="en">
<head>
<meta charset="utf-8">
<title>Silver Birch Helpers – Business Card</title>
<link rel="stylesheet" href="https://fonts.googleapis.com/css2?family=Exo+2:wght@400;500;600&display=swap">
<style>
  :root {
    --backdrop: #e6e6e4;
    --card: #ffffff;
    --green: #127a3f;
    --gold: #7e6d3c;
    --ink: #3a3a3a;
  }
  * { margin: 0; padding: 0; box-sizing: border-box; }
  html, body {
    width: 1200px; height: 771px; overflow: hidden;
    background: var(--backdrop);
    font-family: "Exo 2", Arial, sans-serif;
  }
  .canvas {
    width: 1200px; height: 771px;
    display: flex; align-items: center; justify-content: center; gap: 40px;
  }
  .card {
    position: relative; width: 540px; height: 308px;
    background: var(--card); overflow: hidden;
    box-shadow: 0 4px 14px rgba(0,0,0,.15);
  }
  .card-swoosh { position: absolute; inset: 0; width: 100%; height: 100%; }

  .brand-name {
    font-family: "Exo 2", Arial, sans-serif;
    font-weight: 600; color: var(--green);
    line-height: 1; letter-spacing: .5px;
  }
  .brand-dot { width: 26px; height: 26px; border-radius: 50%; background: var(--gold); flex: none; }

  /* Front */
  .front .brand {
    position: absolute; left: 34px; top: 30px;
    display: flex; align-items: center; gap: 12px;
  }
  .front .brand-name { font-size: 30px; }
  .address {
    position: absolute; left: 36px; top: 86px;
    font-size: 11.5px; color: var(--ink); line-height: 1.45;
  }
  .person { position: absolute; right: 34px; top: 120px; text-align: right; }
  .person-name { font-size: 17px; font-weight: 500; color: var(--green); }
  .person-title { font-size: 11.5px; color: var(--ink); margin-top: 2px; }
  .contact-list {
    position: absolute; right: 34px; top: 178px;
    list-style: none; text-align: right;
    font-size: 11px; color: var(--ink); line-height: 1.75;
  }
  .contact-list li { display: flex; align-items: center; justify-content: flex-end; gap: 6px; }
  .contact-list svg { width: 11px; height: 11px; fill: var(--ink); }

  /* Back */
  .back-content {
    position: absolute; left: 0; right: 0; top: 46px;
    display: flex; flex-direction: column; align-items: center;
  }
  .back .brand-dot { width: 40px; height: 40px; }
  .back .brand-name { font-size: 34px; margin-top: 12px; }
  .slogan {
    margin-top: 10px; font-size: 13px; font-weight: 500;
    color: var(--gold); letter-spacing: 1px;
  }
  .service-list {
    list-style: none; margin-top: 20px; width: 440px;
    display: flex; flex-wrap: wrap; justify-content: center; gap: 4px 16px;
    font-size: 11px; color: var(--ink);
  }
  .service-list li { display: flex; align-items: center; gap: 6px; }
  .service-list li::before {
    content: ""; width: 5px; height: 5px; border-radius: 50%; background: var(--green);
  }
</style>
</head>
<body>
<main class="canvas">

  <section class="card front" aria-label="Card front">
    <svg class="card-swoosh" viewBox="0 0 540 308" preserveAspectRatio="none" aria-hidden="true">
      <path d="M0,150 C120,165 230,220 330,262 C420,298 480,305 540,308 L0,308 Z" fill="var(--green)"/>
      <path d="M0,168 C120,182 230,232 335,272 C420,302 480,306 540,308 L0,308 Z" fill="#ffffff"/>
      <path d="M0,178 C120,192 225,240 330,280 C400,304 470,308 540,308 L0,308 Z" fill="var(--gold)"/>
      <path d="M300,308 C360,300 420,290 470,262 C440,292 400,304 360,308 Z" fill="var(--green)"/>
    </svg>

    <div class="brand">
      <span class="brand-name">Silver Birch Helpers</span>
      <span class="brand-dot"></span>
    </div>

    <p class="address">214 5th floor Plaza<br>Maple Grove Road NYC</p>

    <div class="person">
      <p class="person-name">Darren Whitlow</p>
      <p class="person-title">President</p>
    </div>

    <ul class="contact-list">
      <li>917.284.6051
        <svg viewBox="0 0 12 12"><path d="M2.5 1 L4.5 1 L5 3.5 L3.8 4.4 C4.4 5.8 5.6 7.2 7.4 8 L8.4 6.9 L11 7.5 L11 9.5 C11 10.3 10.3 11 9.5 11 C5 10.7 1.3 7 1 2.5 C1 1.7 1.7 1 2.5 1 Z"/></svg>
      </li>
      <li>917.512.7368
        <svg viewBox="0 0 12 12"><path d="M3.5 0.5 H8.5 A1 1 0 0 1 9.5 1.5 V10.5 A1 1 0 0 1 8.5 11.5 H3.5 A1 1 0 0 1 2.5 10.5 V1.5 A1 1 0 0 1 3.5 0.5 Z M3.6 2 V9 H8.4 V2 Z"/></svg>
      </li>
      <li>Darren@silverbirchhelpers.com
        <svg viewBox="0 0 12 12"><path d="M1 2.5 H11 V9.5 H1 Z M1.8 3.2 L6 6.3 L10.2 3.2 V3 H1.8 Z" fill-rule="evenodd"/></svg>
      </li>
      <li>www.SilverBirchHelpers.com
        <svg viewBox="0 0 12 12"><circle cx="6" cy="6" r="5" fill="none" stroke="var(--ink)" stroke-width="1.2"/><path d="M1 6 H11 M6 1 C3.5 3.5 3.5 8.5 6 11 C8.5 8.5 8.5 3.5 6 1" fill="none" stroke="var(--ink)" stroke-width="1"/></svg>
      </li>
    </ul>
  </section>

  <section class="card back" aria-label="Card back">
    <svg class="card-swoosh" viewBox="0 0 540 308" preserveAspectRatio="none" aria-hidden="true">
      <path d="M540,248 C420,256 300,282 170,308 L200,308 C310,290 430,268 540,258 Z" fill="var(--green)"/>
      <path d="M540,266 C430,274 320,292 230,308 L540,308 Z" fill="var(--gold)"/>
    </svg>

    <div class="back-content">
      <span class="brand-dot"></span>
      <span class="brand-name">Silver Birch Helpers</span>
      <p class="slogan">Our Family. Caring For Yours.</p>
      <ul class="service-list">
        <li>Meal Preparation</li>
        <li>Transportation</li>
        <li>Light Housekeeping</li>
        <li>Bathing Assistance</li>
        <li>Companionship</li>
      </ul>
    </div>
  </section>

</main>
</body>
</html>
```